Modern business card design for professional copywriter

I'd like a business card design that I can use to have my cards printed out by plink.com as a squared corners business card (see artwork and design guidelines here: https://help.plink.com/hc/en-gb/sections/300481726-PLINK-Product-Templates)

The design should be clean and modern and reflect the colours, tone and branding on my website: https://noravestrel.com.au

Target Market(s)

Professionals, B2B small business owners

Industry/Entity Type

Business

Contact Information for Business Card

Nora Vestrel
m: 0427 593 864
e: nora@noravestrel.com.au
w: noravestrel.com.au

Font styles to use
Sans Serif

Requirements
Must have
• Tagline: "Sharp wording for savvy business owners"
• Brand colours: fd8000, 009984, 666666 and black
Nice to have

```html
<!DOCTYPE html>
<html lang="en">
<head>
<meta charset="utf-8">
<title>Nora Vestrel – Business Card</title>
<link rel="stylesheet" href="https://fonts.googleapis.com/css2?family=Questrial&family=Didact+Gothic&display=swap">
<style>
  :root {
    --teal: #009984;
    --teal-light: #2aa992;
    --orange: #fd8000;
    --grey: #666666;
    --ink: #000000;
    --paper: #ffffff;
    --backdrop: #e6e6e6;
  }
  * { box-sizing: border-box; margin: 0; padding: 0; }
  html, body {
    width: 1200px; height: 675px; overflow: hidden;
    background: var(--backdrop);
    font-family: "Questrial", "Didact Gothic", sans-serif;
  }
  .stage { position: relative; width: 1200px; height: 675px; }

  .card {
    position: absolute; top: 183px;
    width: 540px; height: 309px; overflow: hidden;
    box-shadow: 0 6px 18px rgba(0,0,0,.18);
  }

  /* Front */
  .card--front { left: 40px; background: var(--teal-light); }
  .front__map {
    position: absolute; left: 40px; top: 30px; width: 460px; height: 250px;
    background: radial-gradient(ellipse at center, rgba(255,255,255,.16), rgba(255,255,255,0) 70%);
  }
  .front__arc {
    position: absolute; width: 420px; height: 420px; border-radius: 50%;
    background: rgba(255,255,255,.10);
  }
  .front__arc--left { left: -300px; top: -60px; }
  .front__arc--right { right: -300px; top: -60px; }
  .front__sweep {
    position: absolute; left: -60px; top: -330px; width: 660px; height: 470px;
    border-radius: 50%; background: rgba(255,255,255,.08);
  }
  .front__brand {
    position: absolute; left: 0; right: 0; top: 118px;
    display: flex; justify-content: center; align-items: center; gap: 10px;
  }
  .front__brand .brand-mark { background: var(--paper); }
  .front__brand .brand-name { color: var(--paper); font-size: 40px; }
  .front__url {
    position: absolute; left: 0; right: 0; top: 215px;
    text-align: center; color: var(--paper); font-size: 15px; letter-spacing: .5px;
  }

  .brand-mark { width: 22px; height: 22px; display: inline-block; }
  .brand-name { font-family: "Questrial", sans-serif; font-weight: 400; letter-spacing: -.5px; line-height: 1; }

  /* Back */
  .card--back { left: 620px; background: var(--paper); }
  .back__brand {
    position: absolute; left: 0; right: 0; top: 50px;
    display: flex; justify-content: center; align-items: center; gap: 10px;
  }
  .back__brand .brand-mark { background: var(--orange); }
  .back__brand .brand-name { color: var(--teal); font-size: 40px; }

  .back__identity {
    position: absolute; left: 0; top: 172px; width: 310px; height: 78px;
    background: var(--teal); color: var(--paper);
    text-align: center; padding-top: 20px;
  }
  .back__notch {
    position: absolute; left: 150px; top: 172px; width: 0; height: 0;
    border-left: 9px solid transparent; border-right: 9px solid transparent;
    border-top: 9px solid var(--paper);
  }
  .identity__name { font-size: 17px; font-weight: 700; font-family: "Didact Gothic", sans-serif; }
  .identity__role { font-size: 12px; opacity: .85; margin-top: 2px; }

  .back__contact {
    position: absolute; left: 310px; top: 110px; width: 230px; height: 140px;
    background: var(--orange); color: var(--paper);
    padding: 16px 0 0 18px; list-style: none;
  }
  .contact__item { display: flex; align-items: center; gap: 6px; font-size: 12.5px; margin-bottom: 5px; }
  .contact__icon { width: 15px; height: 15px; flex: none; }

  .back__tagline {
    position: absolute; left: 0; right: 0; top: 250px; height: 59px;
    display: flex; align-items: center; justify-content: center;
    color: var(--grey); font-size: 17px; letter-spacing: 1.8px; text-transform: uppercase;
    white-space: nowrap;
  }
  .back__tagline::before {
    content: ""; position: absolute; left: 12px; right: 12px; top: 8px;
    border-top: 1px solid var(--grey); opacity: .35;
  }
</style>
</head>
<body>
<main class="stage">

  <section class="card card--front" aria-label="Business card front">
    <div class="front__map" role="img" aria-label="Faint world map in light teal"></div>
    <div class="front__sweep"></div>
    <div class="front__arc front__arc--left"></div>
    <div class="front__arc front__arc--right"></div>
    <div class="front__brand">
      <span class="brand-mark" aria-hidden="true"></span>
      <span class="brand-name">Nora Vestrel</span>
    </div>
    <p class="front__url">www.noravestrel.com.au</p>
  </section>

  <section class="card card--back" aria-label="Business card back">
    <div class="back__brand">
      <span class="brand-mark" aria-hidden="true"></span>
      <span class="brand-name">Nora Vestrel</span>
    </div>

    <div class="back__identity">
      <p class="identity__name">Nora Vestrel</p>
      <p class="identity__role">Owner</p>
    </div>
    <span class="back__notch" aria-hidden="true"></span>

    <ul class="back__contact">
      <li class="contact__item">
        <svg class="contact__icon" viewBox="0 0 16 16" aria-hidden="true">
          <circle cx="8" cy="8" r="8" fill="#fff"/>
          <rect x="5.5" y="3.5" width="5" height="9" rx="1" fill="none" stroke="#009984" stroke-width="1.2"/>
          <circle cx="8" cy="11" r=".6" fill="#009984"/>
        </svg>
        0427 593 864
      </li>
      <li class="contact__item">
        <svg class="contact__icon" viewBox="0 0 16 16" aria-hidden="true">
          <circle cx="8" cy="8" r="8" fill="#fff"/>
          <rect x="4" y="5" width="8" height="6" fill="none" stroke="#009984" stroke-width="1.2"/>
          <path d="M4 5 L8 8.5 L12 5" fill="none" stroke="#009984" stroke-width="1.2"/>
        </svg>
        nora@noravestrel.com.au
      </li>
      <li class="contact__item">
        <svg class="contact__icon" viewBox="0 0 16 16" aria-hidden="true">
          <circle cx="8" cy="8" r="8" fill="#fff"/>
          <circle cx="8" cy="8" r="4.5" fill="none" stroke="#009984" stroke-width="1.1"/>
          <ellipse cx="8" cy="8" rx="2" ry="4.5" fill="none" stroke="#009984" stroke-width="1"/>
          <line x1="3.5" y1="8" x2="12.5" y2="8" stroke="#009984" stroke-width="1"/>
        </svg>
        www.noravestrel.com.au
      </li>
    </ul>

    <p class="back__tagline">Sharp wording for savvy business owners</p>
  </section>

</main>
</body>
</html>
```